Business card for massage therapy company called Brook Fern Wellness

Need business card for massage therapy company called Brook Fern Wellness. Would like my logo on the front and the back of the card I have 3 options of logos and you can play with what looks better.

Would like this information displayed on the back of the card:

Marcus Ellery
Licensed Massage Therapist
321-555-0147
brookfern-example.com
brookfern_rest_

```html
<!DOCTYPE html>
<html lang="en">
<head>
<meta charset="utf-8">
<title>Brook Fern Wellness – Business Card</title>
<link rel="stylesheet" href="https://fonts.googleapis.com/css2?family=Mulish:wght@400;700&display=swap">
<style>
  :root {
    --sage-green: #5a7350;
    --card-white: #ffffff;
    --ink: #141414;
    --edge-grey: #cfcfcf;
    --page-bg: #ffffff;
  }
  html, body {
    margin: 0;
    padding: 0;
    width: 1200px;
    height: 361px;
    overflow: hidden;
    background: var(--page-bg);
  }
  .card-spread {
    position: relative;
    width: 1200px;
    height: 361px;
    display: flex;
    box-sizing: border-box;
    border: 1px solid var(--edge-grey);
    font-family: "Mulish", "Century Gothic", sans-serif;
    color: var(--ink);
  }
  .card-front {
    width: 600px;
    height: 100%;
    background: var(--sage-green);
    position: relative;
  }
  .card-back {
    width: 600px;
    height: 100%;
    background: var(--card-white);
    position: relative;
  }
  .wordmark {
    position: absolute;
    left: 190px;
    top: 112px;
    display: flex;
    align-items: center;
    gap: 14px;
    color: var(--ink);
    font-weight: 400;
  }
  .wordmark-dot {
    width: 16px;
    height: 16px;
    border-radius: 50%;
    background: var(--ink);
    flex: none;
  }
  .wordmark-text {
    display: flex;
    flex-direction: column;
    align-items: center;
    line-height: 1;
  }
  .wordmark-name {
    font-size: 40px;
    letter-spacing: 0.5px;
  }
  .wordmark-tag {
    margin-top: 12px;
    font-size: 17px;
    letter-spacing: 6px;
  }
  .contact {
    position: absolute;
    left: 258px;
    top: 155px;
    line-height: 1;
  }
  .contact-name {
    font-size: 21px;
    font-weight: 700;
    margin: 0 0 7px;
  }
  .contact-role {
    font-size: 17.5px;
    font-weight: 400;
    margin: 0 0 28px;
  }
  .contact-lines {
    list-style: none;
    margin: 0;
    padding: 0;
    font-size: 17.5px;
  }
  .contact-lines li {
    margin-bottom: 7px;
  }
</style>
</head>
<body>
  <main class="card-spread">
    <section class="card-front">
      <div class="wordmark">
        <span class="wordmark-dot"></span>
        <div class="wordmark-text">
          <span class="wordmark-name">Brook Fern</span>
          <span class="wordmark-tag">WELLNESS</span>
        </div>
      </div>
    </section>
    <section class="card-back">
      <div class="contact">
        <p class="contact-name">Marcus Ellery</p>
        <p class="contact-role">Licensed Massage Therapist</p>
        <ul class="contact-lines">
          <li>321-555-0147</li>
          <li>brookfern-example.com</li>
          <li>brookfern_rest_</li>
        </ul>
      </div>
    </section>
  </main>
</body>
</html>
```